Brightwell Giving Inc

We need a full re-design of our non-profit organization website (www.brightwellgiving.org). Ideally, we are looking to make it more attractive, user-friendly, and interactive with our business model.

Please make sure to user colors that ago with our logo.

We need a homepage done and we also need a content page done where we will use for the other pages to fill with content.

Target Market(s)

Clothes/textiles donations.

Industry/Entity Type

Charity

Number of Pages Required

2 page

Colors

Designer to choose colors to be used in the design.

Requirements
Must have
• It must match the styling of our logo and same colors as current website. (www.brightwellgiving.org)
Nice to have
• Sleek homepage that is easy to understand and get our main points across.

```html
<!DOCTYPE html>
<html lang="en">
<head>
<meta charset="utf-8">
<title>Brightwell Giving – Our Mission</title>
<link rel="stylesheet" href="https://fonts.googleapis.com/css2?family=Lato:wght@400;700&family=Mulish:wght@400;600&display=swap">
<style>
:root{
  --green:#23881a;
  --green-dark:#1d6514;
  --green-deep:#173e0f;
  --yellow:#fcd21f;
  --yellow-light:#fde53e;
  --orange:#f9a11b;
  --ink:#1e2a14;
  --white:#ffffff;
}
*{margin:0;padding:0;box-sizing:border-box}
html,body{width:830px;height:1200px;overflow:hidden;background:var(--white)}
body{position:relative;font-family:"Mulish",sans-serif;color:var(--ink)}
.abs{position:absolute}
.top-rule{left:0;top:0;width:830px;height:4px;background:var(--yellow)}
.phone-tab{left:619px;top:0;width:128px;height:30px;background:var(--yellow);border-radius:0 0 3px 3px;
  font-family:"Lato",sans-serif;font-weight:700;font-size:13px;display:flex;align-items:center;justify-content:center;gap:4px;color:var(--ink)}
.brand{left:82px;top:34px;display:flex;align-items:center;gap:8px}
.brand-mark{width:30px;height:30px;background:var(--green)}
.brand-name{font-family:"Lato",sans-serif;font-weight:700;font-size:14px;color:var(--green-deep);letter-spacing:.3px;line-height:1}
.nav{left:277px;top:39px;display:flex;align-items:center;gap:18.5px;font-family:"Lato",sans-serif;font-size:12.6px;color:var(--ink)}
.nav-home{width:25px;height:25px;border-radius:50%;background:var(--green);display:flex;align-items:center;justify-content:center}
.hero{left:0;top:82px;width:830px;height:320px;background:linear-gradient(100deg,#7d7d88 0%,#6b5a6f 30%,#8a8a8e 55%,#a7a9a6 100%)}
.hero-title{left:0;top:182px;width:830px;text-align:center;font-family:"Mulish",sans-serif;font-weight:600;font-size:37px;color:var(--white);letter-spacing:.5px}
.mission-title{left:0;top:406px;width:830px;text-align:center;font-size:22px;font-weight:600;color:var(--green-deep)}
.mission-text{left:112px;top:447px;width:606px;text-align:center;font-size:11.2px;line-height:19.4px}
.impact{left:0;top:588px;width:830px;height:350px;background:linear-gradient(180deg,var(--yellow-light) 0%,var(--yellow) 45%,var(--orange) 100%)}
.impact-title{left:98px;top:676px;font-size:26px;font-weight:400;color:var(--ink)}
.impact-text{left:100px;top:720px;width:410px;height:166px;overflow:hidden;font-size:10.4px;line-height:18.4px}
.impact-ring{left:515px;top:672px;width:224px;height:224px;border-radius:50%;border:5px solid var(--white);padding:4px}
.impact-photo{width:100%;height:100%;border-radius:50%;background:radial-gradient(circle at 40% 45%,#c9c3b2,#7a9a6a 70%,#4f7a3c)}
.footer{left:0;top:937px;width:830px;height:263px;background:var(--green);color:var(--white)}
.f-head{font-size:13px;letter-spacing:.2px}
.f-list{list-style:none;font-size:10px;line-height:19.5px}
.f-rule{width:1px;height:116px;background:rgba(255,255,255,.3)}
.contact-row{display:flex;gap:8px;font-size:9.6px;line-height:18.8px;align-items:flex-start}
.zip{left:564px;top:997px;width:181px;height:26px;background:var(--green-deep);font-size:10px;padding:0 12px;display:flex;align-items:center}
.search{left:565px;top:1032px;width:88px;height:25px;background:linear-gradient(var(--orange),#f58a12);font-family:"Lato",sans-serif;font-weight:700;font-size:12px;display:flex;align-items:center;justify-content:center}
.social{top:1067px;width:26px;height:26px;border-radius:50%;border:1.5px solid var(--white)}
.bottom-rule{left:98px;top:1148px;width:650px;height:1px;background:rgba(255,255,255,.25)}
.copyright{left:0;top:1163px;width:830px;text-align:center;font-size:8.5px;color:rgba(255,255,255,.75)}
</style>
</head>
<body>
<div class="abs top-rule"></div>
<div class="abs phone-tab">
  <svg width="12" height="12" viewBox="0 0 24 24"><path fill="#1d6514" d="M6.6 10.8a15 15 0 0 0 6.6 6.6l2.2-2.2c.3-.3.7-.4 1-.2 1.1.4 2.3.6 3.6.6.6 0 1 .4 1 1V20c0 .6-.4 1-1 1A17 17 0 0 1 3 4c0-.6.4-1 1-1h3.5c.6 0 1 .4 1 1 0 1.3.2 2.5.6 3.6.1.3 0 .7-.2 1z"/></svg>
  (855) 410-3386
</div>

<div class="abs brand">
  <div class="brand-mark"></div>
  <div class="brand-name">BRIGHTWELL GIVING</div>
</div>

<nav class="abs nav">
  <span class="nav-home"><svg width="12" height="12" viewBox="0 0 24 24"><path fill="#fff" d="M12 3 2 12h3v8h5v-6h4v6h5v-8h3z"/></svg></span>
  <span>Mission</span><span>Family</span><span>How it Works</span><span>About Us</span><span>News</span><span>Donate</span><span>Sponsors</span>
</nav>

<div class="abs hero" role="img" aria-label="Smiling girl and volunteers sorting donated clothes"></div>
<svg class="abs" style="left:0;top:330px" width="830" height="75" viewBox="0 0 830 75">
  <path d="M0 68 Q415 -40 830 63 L830 75 L0 75 Z" fill="#fcc315"/>
  <path d="M0 72 Q415 -28 830 72 L830 75 L0 75 Z" fill="#fff"/>
</svg>
<h1 class="abs hero-title">OUR MISSION</h1>

<h2 class="abs mission-title">Mission Statement</h2>
<p class="abs mission-text">Brightwell Giving has a two part mission to help local communities while helping the planet. The average American discards 68 lbs of clothing annually. That is 1,325,340,196 lbs for New York State alone and 21,202,400,000 lbs for the U.S. every year! By keeping unwanted clothes out of the trash can we are greatly reducing the amount of material that enters our landfills. We are also turning the unwanted clothes into funding for our local communities. We are asking for your help to increase local support. Simply put, there is no better time to act than now.</p>

<section class="abs impact"></section>
<svg class="abs" style="left:0;top:586px" width="830" height="40" viewBox="0 0 830 40">
  <path d="M0 0 L830 0 L830 2 Q415 64 0 2 Z" fill="#fff"/>
</svg>
<h2 class="abs impact-title">Impact Statement</h2>
<p class="abs impact-text">In such trying times as these, the only people we can turn to for help are each other. Nothing is greater than the desire of a community to help its own. Brightwell Giving is dedicated to becoming an active member of the community by providing for its less fortunate members. Our goal is to differentiate ourselves from other charitable organizations by running a transparent operation that makes the most of its donations. Our plan is to run an “open book” charity wherein all of our operations and accounting system are fully disclosed to the public. This will allow the community and its donors to see where your donations are going. Anyone will be able to review the operating costs of our organization in order to ensure that we are making the most of every gift.</p>
<div class="abs impact-ring"><div class="impact-photo" role="img" aria-label="Volunteers packing donation boxes outdoors"></div></div>

<footer class="abs footer"></footer>
<div class="abs" style="left:90px;top:975px">
  <div class="f-head" style="color:#fff">QUICK LINKS</div>
  <ul class="f-list" style="color:#fff;margin-top:8px"><li>About Us</li><li>Mission</li><li>Family</li><li>How it Works</li></ul>
</div>
<div class="abs f-rule" style="left:193px;top:975px"></div>
<div class="abs" style="left:224px;top:975px">
  <div class="f-head" style="color:#fff">RESOURCES</div>
  <ul class="f-list" style="color:#fff;margin-top:8px"><li>News</li><li>Donate</li><li>Sponsors</li><li>Contact Us</li></ul>
</div>
<div class="abs f-rule" style="left:324px;top:975px"></div>
<div class="abs" style="left:358px;top:973px;color:#fff">
  <div class="f-head">CONTACT US</div>
  <div style="margin-top:8px">
    <div class="contact-row"><svg width="10" height="13" viewBox="0 0 24 32" style="margin-top:3px"><path fill="#fff" d="M12 0a12 12 0 0 0-12 12c0 9 12 20 12 20s12-11 12-20A12 12 0 0 0 12 0zm0 17a5 5 0 1 1 0-10 5 5 0 0 1 0 10z"/></svg><span>42 Orchard Ln Hudson<br>NY 12534</span></div>
    <div class="contact-row"><svg width="11" height="11" viewBox="0 0 24 24" style="margin-top:3px"><path fill="#fff" d="M6.6 10.8a15 15 0 0 0 6.6 6.6l2.2-2.2c.3-.3.7-.4 1-.2 1.1.4 2.3.6 3.6.6.6 0 1 .4 1 1V20c0 .6-.4 1-1 1A17 17 0 0 1 3 4c0-.6.4-1 1-1h3.5c.6 0 1 .4 1 1 0 1.3.2 2.5.6 3.6.1.3 0 .7-.2 1z"/></svg><span>986.555.0148</span></div>
    <div class="contact-row"><svg width="11" height="9" viewBox="0 0 24 18" style="margin-top:4px"><path fill="#fff" d="M0 0h24v2L12 9 0 2zm0 4 12 7 12-7v14H0z"/></svg><span>hello@brightwellgiving.org</span></div>
  </div>
</div>
<div class="abs f-rule" style="left:535px;top:975px"></div>
<div class="abs f-head" style="left:563px;top:973px;color:#fff">FIND DONATION PLACE</div>
<div class="abs zip" style="color:#fff">Zip Code</div>
<div class="abs search" style="color:#fff">Search</div>
<div class="abs social" style="left:564px" aria-label="Social profile"></div>
<div class="abs social" style="left:594px" aria-label="Social profile"></div>
<div class="abs social" style="left:624px" aria-label="Social profile"></div>
<div class="abs social" style="left:654px" aria-label="Social profile"></div>
<div class="abs bottom-rule"></div>
<div class="abs copyright">© 2018 Company Name  All right reserved</div>
</body>
</html>
```